81M business card

I need a business card for a life sciences consulting firm I started. The company name is 81M and the logo is attached. I am looking for something edgey and current but different from the blah standard business card.

Industry/Entity Type

Business

Requirements
Nice to have
• Both sides

```html
<!DOCTYPE html>
<html lang="en">
<head>
<meta charset="utf-8">
<title>81M Business Card</title>
<link rel="stylesheet" href="https://fonts.googleapis.com/css2?family=Open+Sans:wght@400;600;700&display=swap">
<style>
  :root {
    --page: #e9e7e4;
    --card: #ffffff;
    --card-edge: #ececef;
    --navy: #23317a;
    --blue: #1f4fa0;
    --orange: #f08a1c;
    --orange-deep: #e8541e;
    --grey-text: #6b6b6b;
    --faint: #eceef4;
  }
  * { margin: 0; padding: 0; box-sizing: border-box; }
  html, body { width: 1200px; height: 900px; overflow: hidden; }
  body {
    background: var(--page);
    font-family: "Open Sans", Arial, sans-serif;
    position: relative;
  }
  .card {
    position: absolute;
    width: 590px;
    height: 340px;
    border-radius: 18px;
    background: linear-gradient(160deg, #ffffff 0%, #ffffff 55%, #eeeeef 100%);
    border: 1px solid var(--card-edge);
    overflow: hidden;
  }
  .card-front { left: 143px; top: 98px; }
  .card-back { left: 523px; top: 486px; }

  .brand { position: absolute; display: flex; align-items: center; gap: 10px; }
  .brand-mark { width: 52px; height: 52px; border-radius: 50%; background: var(--blue); }
  .brand-name {
    font-weight: 700;
    font-size: 38px;
    letter-spacing: 1px;
    color: var(--navy);
    line-height: 1;
  }
  .tagline {
    position: absolute;
    font-size: 11.5px;
    color: var(--grey-text);
    white-space: nowrap;
  }
  .card-front .brand { left: 46px; top: 216px; }
  .card-front .tagline { left: 35px; top: 280px; }

  .hero-art { position: absolute; left: 290px; top: 20px; width: 300px; height: 320px; }
  .back-art { position: absolute; left: 0; top: 30px; width: 300px; height: 310px; }

  .holder { position: absolute; left: 30px; top: 166px; }
  .holder-name { font-size: 14px; font-weight: 700; color: var(--blue); line-height: 1.1; }
  .holder-role { font-size: 9px; font-weight: 600; color: var(--orange-deep); margin-left: 12px; }

  .contacts { position: absolute; left: 114px; top: 228px; list-style: none; }
  .contacts li {
    display: flex; align-items: center; gap: 8px;
    font-size: 11px; font-weight: 600; color: var(--blue);
    height: 21px;
  }
  .contacts svg { width: 10px; height: 12px; }
  .contacts .at { font-size: 11px; color: var(--orange-deep); width: 10px; text-align: center; }

  .card-back .brand { left: 350px; top: 202px; }
  .card-back .tagline { left: 338px; top: 270px; }
</style>
</head>
<body>
  <section class="card card-front">
    <svg class="hero-art" viewBox="0 0 300 320" role="img" aria-label="Large brand emblem decoration">
      <defs>
        <linearGradient id="heroFill" x1="0" y1="0" x2="0.4" y2="1">
          <stop offset="0" stop-color="#1f4fa0"/>
          <stop offset="0.6" stop-color="#23317a"/>
          <stop offset="1" stop-color="#e8541e"/>
        </linearGradient>
      </defs>
      <circle cx="165" cy="170" r="162" fill="url(#heroFill)"/>
    </svg>
    <div class="brand">
      <span class="brand-mark"></span>
      <span class="brand-name">81M LLC</span>
    </div>
    <p class="tagline">regulatory consulting and contract services</p>
  </section>

  <section class="card card-back">
    <svg class="back-art" viewBox="0 0 300 310" role="img" aria-label="Faint brand emblem decoration">
      <circle cx="140" cy="165" r="150" fill="var(--faint)"/>
    </svg>
    <div class="holder">
      <p class="holder-name">Daniel Ross</p>
      <p class="holder-role">general manager</p>
    </div>
    <ul class="contacts">
      <li>
        <svg viewBox="0 0 10 12" aria-hidden="true">
          <rect x="1.5" y="0.5" width="7" height="11" rx="1.2" fill="none" stroke="#e8541e" stroke-width="1.2"/>
          <circle cx="5" cy="9.4" r="0.8" fill="#e8541e"/>
        </svg>
        <span>0400 555 218</span>
      </li>
      <li>
        <span class="at">@</span>
        <span>danielross@81m.com</span>
      </li>
    </ul>
    <div class="brand">
      <span class="brand-mark"></span>
      <span class="brand-name">81M LLC</span>
    </div>
    <p class="tagline">regulatory consulting and contract services</p>
  </section>
</body>
</html>
```